BRIARFELL Real Estate
Real Estate Developer
Project: BRIARFELL Real Estate
BRIARFELL Real Estate - Real Estate
Creative Brief
Use specific fonts
Up to the designer!
Professional
Matthias L. Halvik
Managing Director
BRIARFELL Real Estate GmbH & Co. KG Lindauer Gang 14 20417 Hamburg Germany
mlh@briarfellre.com
briarfellre.com
One-sided or two-sided cards are welcome and any of the three logos and its colour variations can be chosen!

```html
<!DOCTYPE html>
<html lang="de">
<head>
<meta charset="utf-8">
<title>BRIARFELL Real Estate – Business Cards</title>
<link rel="stylesheet" href="https://fonts.googleapis.com/css2?family=Montserrat:wght@700&family=Open+Sans:wght@400;600&display=swap">
<style>
  :root {
    --bg: #e6e7e6;
    --card: #ffffff;
    --green: #1e4a2b;
    --ink: #4a4d4b;
    --muted: #7a7d7b;
    --rule: #d3d6d4;
  }
  * { box-sizing: border-box; margin: 0; padding: 0; }
  html, body { width: 1200px; height: 852px; overflow: hidden; }
  body {
    background: var(--bg);
    font-family: "Open Sans", Arial, sans-serif;
    color: var(--ink);
    position: relative;
  }
  .card {
    position: absolute;
    width: 520px;
    height: 300px;
    background: var(--card);
    border-radius: 14px;
    border-bottom: 12px solid var(--green);
    box-shadow: 0 6px 18px rgba(0,0,0,0.12);
    overflow: hidden;
  }
  .card--split { left: 50px; top: 276px; }
  .card--stacked { left: 630px; top: 276px; }

  .wordmark { text-align: center; }
  .wordmark__dot { width: 34px; height: 34px; border-radius: 50%; background: var(--green); margin: 0 auto 10px; }
  .wordmark__name {
    font-family: "Open Sans", Arial, sans-serif;
    font-weight: 600;
    font-size: 17px;
    color: var(--green);
    line-height: 1.2;
    white-space: nowrap;
  }

  .person__name { font-family: "Montserrat", Arial, sans-serif; font-weight: 700; font-size: 14px; color: var(--green); }
  .person__role { font-size: 10px; font-weight: 600; color: var(--ink); margin-top: 3px; }
  .person__address { font-size: 9.5px; color: var(--muted); line-height: 1.45; margin-top: 12px; }

  .contacts { list-style: none; font-size: 9.5px; color: var(--ink); }
  .contacts li { display: flex; align-items: center; gap: 8px; height: 15px; }
  .contacts svg { width: 10px; height: 10px; fill: var(--ink); flex: none; }

  /* split card */
  .card--split .wordmark { position: absolute; left: 20px; top: 108px; width: 220px; }
  .card--split .divider { position: absolute; left: 250px; top: 38px; width: 1px; height: 220px; background: var(--rule); }
  .card--split .details { position: absolute; left: 270px; top: 44px; }
  .card--split .contacts { margin-top: 18px; }

  /* stacked card */
  .card--stacked .wordmark { position: absolute; left: 0; right: 0; top: 52px; }
  .card--stacked .person { position: absolute; left: 70px; top: 170px; width: 175px; }
  .card--stacked .divider { position: absolute; left: 258px; top: 168px; width: 1px; height: 90px; background: var(--rule); }
  .card--stacked .contacts { position: absolute; left: 275px; top: 170px; }
</style>
</head>
<body>
  <svg width="0" height="0" style="position:absolute">
    <symbol id="i-phone" viewBox="0 0 24 24"><path d="M6.6 10.8a15 15 0 0 0 6.6 6.6l2.2-2.2c.3-.3.7-.4 1-.2 1.1.4 2.3.6 3.6.6.6 0 1 .4 1 1V20c0 .6-.4 1-1 1A17 17 0 0 1 3 4c0-.6.4-1 1-1h3.5c.6 0 1 .4 1 1 0 1.3.2 2.5.6 3.6.1.3 0 .7-.2 1z"/></symbol>
    <symbol id="i-mobile" viewBox="0 0 24 24"><path d="M7 1h10a2 2 0 0 1 2 2v18a2 2 0 0 1-2 2H7a2 2 0 0 1-2-2V3a2 2 0 0 1 2-2zm0 3v14h10V4zm5 15.5a1.2 1.2 0 1 0 0 2.4 1.2 1.2 0 0 0 0-2.4z"/></symbol>
    <symbol id="i-fax" viewBox="0 0 24 24"><path d="M6 2h9l3 3v5H6zM3 11h18a1 1 0 0 1 1 1v9a1 1 0 0 1-1 1H3a1 1 0 0 1-1-1v-9a1 1 0 0 1 1-1zm3 3v2h3v-2zm5 0v2h3v-2zm-5 4v2h3v-2zm5 0v2h3v-2z"/></symbol>
    <symbol id="i-mail" viewBox="0 0 24 24"><path d="M2 5h20v14H2zm2 2v.5l8 5 8-5V7zm0 2.8V17h16V9.8l-8 5z"/></symbol>
  </svg>

  <article class="card card--split">
    <div class="wordmark">
      <div class="wordmark__dot"></div>
      <div class="wordmark__name">BRIARFELL Real Estate</div>
    </div>
    <div class="divider"></div>
    <div class="details">
      <div class="person">
        <div class="person__name">Matthias L. Halvik</div>
        <div class="person__role">Managing Director</div>
        <div class="person__address">Lindauer Gang 14<br>20417 Hamburg, Germany</div>
      </div>
      <ul class="contacts">
        <li><svg><use href="#i-phone"/></svg>+49 (0)40 5550182</li>
        <li><svg><use href="#i-mobile"/></svg>+49 (0)175 5550647</li>
        <li><svg><use href="#i-fax"/></svg>+49 (0)40 5550183</li>
        <li><svg><use href="#i-mail"/></svg>mlh@briarfellre.com</li>
      </ul>
    </div>
  </article>

  <article class="card card--stacked">
    <div class="wordmark">
      <div class="wordmark__dot"></div>
      <div class="wordmark__name">BRIARFELL Real Estate</div>
    </div>
    <div class="person">
      <div class="person__name">Matthias L. Halvik</div>
      <div class="person__role">Managing Director</div>
      <div class="person__address">Lindauer Gang 14<br>20417 Hamburg, Germany</div>
    </div>
    <div class="divider"></div>
    <ul class="contacts">
      <li><svg><use href="#i-phone"/></svg>+49 (0)40 5550182</li>
      <li><svg><use href="#i-mobile"/></svg>+49 (0)175 5550647</li>
      <li><svg><use href="#i-fax"/></svg>+49 (0)40 5550183</li>
      <li><svg><use href="#i-mail"/></svg>mlh@briarfellre.com</li>
    </ul>
  </article>
</body>
</html>
```